Bryncarn foot health or foot health bryncarn

Treatments in comfort of your own home
Delia Marsh cert KTLFr Pod, BGNVect
Treatments will be listed on the leaflet I will attach
I am a Foot Health practitioner,
I want to mention I do home visits throughout Pembrokeshire & Ceredigion.
Tel. 07730915264
I have 2 logs to forward to you they are the associations I belong to .
One of which is also a certification mark. It is important that the same colour is used for this mark. They are not the main focus, they are just recognised mark. To be at the top or bottom of the page.
There is a local business called Glenmorrow foot clinic, so my business has to be bryncarn foot health, or foot health bryncarn
soon I will also need a web page and cards designed, so please keep this in mind when designing the Artwork. I will also need an email on the leaflet but I will wait and see what the design is first before I confirm it as I have several.
I hope this is enough info for you.
Many thanks,
Delia Marsh

Target Market(s)

Mostly the elderly, some middle age women, but it is a service for all ages. The elderly are my main clients.

Industry/Entity Type

Health

Font styles to use
Serif
Sans Serif

Colors

Designer to choose colors to be used in the design.

Requirements
Must have
• Covering Pembrokeshire & Ceredigion.
Treatments include:- as listed on example leaflet I sent
Phone number a size that's easily readable.
I am open to colours. I love bright colours, but also like the more conservative colours as long as it looks professional. I'm wanting it to look more up market.
Nice to have
• Logo for Covenant and KTS logo obviously smaller, but also recognisable and either at the top of page or bottom. These are not to be main focal point.

```html
<!DOCTYPE html>
<html lang="en">
<head>
<meta charset="utf-8">
<title>Bryncarn Foot Health – Delia Marsh</title>
<link href="https://fonts.googleapis.com/css2?family=Montserrat:wght@600;700&family=Questrial&display=swap" rel="stylesheet">
<style>
  :root {
    --slate: #68686d;
    --slate-dark: #5d5d62;
    --lemon: #e9e36c;
    --sky: #4fb4d0;
    --white: #ffffff;
    --strip: #b9b9bd;
    --pale-lemon: #eeeb92;
  }
  * { margin: 0; padding: 0; box-sizing: border-box; }
  html, body { width: 846px; height: 1200px; overflow: hidden; }
  body { background: var(--slate); }
  .leaflet {
    position: relative;
    width: 846px;
    height: 1200px;
    background: radial-gradient(ellipse at 50% 40%, var(--slate) 55%, var(--slate-dark) 100%);
    font-family: "Montserrat", Arial, sans-serif;
    text-align: center;
    overflow: hidden;
  }
  .business-name {
    position: absolute; top: 56px; left: 0; width: 100%;
    color: var(--lemon); font-weight: 600; font-size: 52px; letter-spacing: 3px;
    white-space: nowrap;
  }
  .practitioner {
    position: absolute; top: 152px; left: 0; width: 100%;
    color: var(--white); font-weight: 700; font-size: 33px; letter-spacing: 1.2px;
    white-space: nowrap;
  }
  .coverage {
    position: absolute; top: 204px; left: 0; width: 100%;
    color: var(--lemon); font-weight: 700; font-size: 24px; letter-spacing: 0.5px;
    white-space: nowrap;
  }
  .phone-box {
    position: absolute; top: 258px; left: 200px; width: 447px; height: 83px;
    background: var(--white); border-radius: 14px;
    display: flex; align-items: center; justify-content: center;
  }
  .phone-number {
    color: var(--sky); font-weight: 700; font-size: 43px; letter-spacing: 2px;
  }
  .treatments-title {
    position: absolute; top: 378px; left: 0; width: 100%;
    color: var(--sky); font-weight: 700; font-size: 42px; letter-spacing: 1.5px;
    text-decoration: underline; text-decoration-thickness: 3px; text-underline-offset: 8px;
  }
  .treatment-list {
    position: absolute; top: 449px; left: 0; width: 100%;
    list-style: none; color: var(--white);
    font-family: "Questrial", "Century Gothic", sans-serif; font-size: 53px; line-height: 67.5px;
    white-space: nowrap;
  }
  .treatment-list li::before { content: "· "; }
  .home-note {
    position: absolute; top: 869px; left: 0; width: 100%;
    color: var(--sky); font-weight: 700; font-size: 29px; letter-spacing: 0.9px;
    text-decoration: underline; text-decoration-thickness: 2px; text-underline-offset: 5px;
    white-space: nowrap;
  }
  .photo-strip {
    position: absolute; top: 925px; left: 0; width: 846px; height: 158px;
    background: var(--strip);
  }
  .photo { position: absolute; top: 12px; height: 133px; }
  .photo--sandals { left: 8px; width: 247px; background: linear-gradient(135deg, #8ea35a, #c79a78 60%, #6e7d3a); }
  .photo--lotus { left: 267px; width: 211px; background: linear-gradient(135deg, #e9d9c6, #e88aa4 55%, #f1e7dc); }
  .photo--daisies { left: 487px; width: 171px; background: linear-gradient(135deg, #fafafa, #f0b8c0 50%, #ffffff); }
  .photo--legs { left: 673px; width: 152px; background: linear-gradient(90deg, #5a3a22, #c98e5e 50%, #4a3020); }
  .badge-register {
    position: absolute; left: 0; top: 1108px; width: 218px; height: 82px; background: var(--white);
  }
  .badge-register .mark { position: absolute; left: 14px; top: 14px; width: 54px; height: 54px; border-radius: 50%; background: #6a3c8e; }
  .badge-covenant {
    position: absolute; left: 730px; top: 1103px; width: 98px; height: 93px; background: var(--white);
  }
  .badge-covenant .mark { position: absolute; left: 14px; top: 8px; width: 70px; height: 70px; border-radius: 50%; background: #3d5a3a; }
  .footer-bar {
    position: absolute; left: 240px; top: 1184px; width: 360px; height: 16px; background: var(--pale-lemon);
  }
</style>
</head>
<body>
<main class="leaflet">
  <h1 class="business-name">BRYNCARN FOOT HEALTH</h1>
  <p class="practitioner">DELIA MARSH KTLFr, BGNVect (FHP)</p>
  <p class="coverage">home visits throughout Pembrokeshire &amp; Ceredigion.</p>
  <div class="phone-box"><span class="phone-number">07730 91 52 64</span></div>
  <h2 class="treatments-title">TREATMENTS INCLUDE</h2>
  <ul class="treatment-list">
    <li>Diabetic foot care</li>
    <li>Ingrowing toenails</li>
    <li>Corn &amp; callous treatment</li>
    <li>Toenail clipping</li>
    <li>Fungal infections treated</li>
    <li>Cracked heels</li>
  </ul>
  <p class="home-note">Treatments in comfort of your own home</p>
  <section class="photo-strip">
    <div class="photo photo--sandals" role="img" aria-label="Photo of feet in sandals on grass"></div>
    <div class="photo photo--lotus" role="img" aria-label="Photo of a foot massage with pink lotus flowers"></div>
    <div class="photo photo--daisies" role="img" aria-label="Photo of feet with pink gerbera flowers"></div>
    <div class="photo photo--legs" role="img" aria-label="Photo of bare legs and feet"></div>
  </section>
  <div class="badge-register" role="img" aria-label="Certification mark badge"><span class="mark"></span></div>
  <div class="badge-covenant" role="img" aria-label="Association membership badge"><span class="mark"></span></div>
  <div class="footer-bar"></div>
</main>
</body>
</html>
```